Visitenkarten-Design für Verkäufer von Honig und Honigprodukten
Zielgruppe
Verkauf von Manuka Honig und Honigprodukte - siehe www.korimuta.de
Aufgabenstellung
Keine bestimmten Vorgaben. Angaben für die Visitenkarten hier:
https://www.korimuta.de/impressum/
Firmenname soll Korimuta.de GbR werden (wird in Kürze eingetragen)

```html
<!DOCTYPE html>
<html lang="de">
<head>
<meta charset="utf-8">
<title>Korimuta.de Visitenkarten</title>
<link rel="stylesheet" href="https://fonts.googleapis.com/css2?family=Open+Sans:wght@400;600;700&display=swap">
<style>
  :root {
    --bg: #ece8e2;
    --brown: #7a5a3a;
    --gold: #f4cf82;
    --gold-text: #f2c66a;
    --white: #ffffff;
    --ink: #1d1a17;
  }
  * { box-sizing: border-box; margin: 0; padding: 0; }
  html, body { width: 1200px; height: 912px; overflow: hidden; }
  body {
    background: var(--bg);
    font-family: "Open Sans", Arial, sans-serif;
    position: relative;
  }
  .card {
    position: absolute;
    left: 290px;
    width: 620px;
    height: 400px;
    overflow: hidden;
    box-shadow: 0 6px 18px rgba(0,0,0,.18);
  }
  /* Front */
  .card-front { top: 40px; background: var(--brown); }
  .front-deco {
    position: absolute; left: 150px; top: 20px;
    width: 340px; height: 340px; border-radius: 50%;
    border: 26px solid rgba(255,255,255,.05);
  }
  .front-brand {
    position: absolute; left: 0; right: 0; top: 150px;
    display: flex; align-items: center; justify-content: center; gap: 16px;
  }
  .brand-dot { width: 34px; height: 34px; border-radius: 50%; background: var(--gold); }
  .front-brand .brand-name {
    color: var(--white); font-size: 58px; font-weight: 400; letter-spacing: 1px;
  }
  .front-web {
    position: absolute; left: 0; right: 0; top: 272px;
    text-align: center; color: var(--white); font-size: 15px; letter-spacing: .5px;
  }
  /* Back */
  .card-back { top: 472px; background: var(--gold); }
  .back-shapes { position: absolute; inset: 0; }
  .back-brand {
    position: absolute; left: 60px; top: 108px;
    display: flex; align-items: center; gap: 12px;
  }
  .back-brand .brand-dot { width: 28px; height: 28px; }
  .back-brand .brand-name { color: var(--brown); font-size: 48px; font-weight: 400; }
  .person { position: absolute; left: 62px; top: 190px; }
  .person-name { color: var(--gold-text); font-size: 22px; font-weight: 700; }
  .person-role { color: var(--ink); font-size: 15px; margin-top: 2px; }
  .address {
    position: absolute; left: 62px; top: 346px;
    color: var(--white); font-size: 15px; line-height: 1.45;
  }
  .contacts {
    position: absolute; left: 440px; top: 190px;
    list-style: none; color: var(--white); font-size: 13.5px;
  }
  .contacts li { display: flex; align-items: center; gap: 9px; height: 22px; }
  .contacts svg { width: 14px; height: 14px; flex: none; }
</style>
</head>
<body>

<section class="card card-front" aria-label="Visitenkarte Vorderseite">
  <div class="front-deco" aria-hidden="true"></div>
  <div class="front-brand">
    <span class="brand-dot" aria-hidden="true"></span>
    <span class="brand-name">korimuta.de</span>
  </div>
  <p class="front-web">www.korimuta.de</p>
</section>

<section class="card card-back" aria-label="Visitenkarte Rückseite">
  <svg class="back-shapes" viewBox="0 0 620 400" width="620" height="400" aria-hidden="true">
    <path d="M0,0 H500 C450,150 300,285 0,322 Z" fill="var(--white)"/>
    <path d="M478,28 C440,170 290,292 0,328 L0,342 C300,312 455,190 478,28 Z" fill="var(--brown)"/>
  </svg>

  <div class="back-brand">
    <span class="brand-dot" aria-hidden="true"></span>
    <span class="brand-name">korimuta.de</span>
  </div>

  <div class="person">
    <p class="person-name">Lukas Brenneisen</p>
    <p class="person-role">Geschäftsführer</p>
  </div>

  <p class="address">Lindenweg 12<br>00000 Talbergen, Deutschland</p>

  <ul class="contacts">
    <li>
      <svg viewBox="0 0 16 16"><path fill="var(--brown)" d="M3 1l3 3-2 2c1 2 3 4 5 5l2-2 3 3-2 3C7 14 2 9 1 3z"/></svg>
      01234-4418820
    </li>
    <li>
      <svg viewBox="0 0 16 16"><rect x="4" y="1" width="8" height="14" rx="1.5" fill="none" stroke="var(--brown)" stroke-width="1.8"/></svg>
      01234-4418800
    </li>
    <li>
      <svg viewBox="0 0 16 16"><rect x="4" y="1" width="8" height="5" fill="var(--brown)"/><rect x="1" y="6" width="14" height="6" fill="var(--brown)"/><rect x="4" y="11" width="8" height="4" fill="var(--brown)"/></svg>
      01234-4418824
    </li>
    <li>
      <svg viewBox="0 0 16 16"><rect x="1" y="3" width="14" height="10" fill="var(--brown)"/><path d="M1 3l7 6 7-6" fill="none" stroke="var(--gold)" stroke-width="1.2"/></svg>
      info@korimuta.de
    </li>
    <li>
      <svg viewBox="0 0 16 16"><circle cx="8" cy="8" r="7" fill="var(--brown)"/><path d="M1 8h14M8 1c-3 4-3 10 0 14M8 1c3 4 3 10 0 14" fill="none" stroke="var(--gold)" stroke-width="1"/></svg>
      www.korimuta.de
    </li>
  </ul>
</section>

</body>
</html>
```